Healer at the Hearth needs business card

We need a business card that reflects the look and feel of the new website at www.healerathearth.ca

Target Market(s)

Our patient navigation and advocacy services are most commonly used by seniors who feel overwhelmed by the health care system and want someone on their side to advocate for their care. Individuals with ill parents or other family members may also come to rely on Healer at the Hearth to help them support their loved one through their health care journey. Ultimately, anyone who finds their health care experience challenging and wants someone completely focused on their needs can benefit from the services of our doctor / nurse team.

Industry/Entity Type

Business

Requirements
Must have
• One design tailored for two clinician which should include: logo, name, title, tel, email, web address and tagline
Nice to have
• A banner image to create a similar look to the website at www.healerathearth.ca
Should not have
• Too cluttered or busy - must be clean and professional

```html
<!DOCTYPE html>
<html lang="en">
<head>
<meta charset="UTF-8">
<title>Healer at the Hearth – Business Card</title>
<link href="https://fonts.googleapis.com/css2?family=Montserrat:wght@400;500;600&display=swap" rel="stylesheet">
<style>
  :root {
    --backdrop: #3b4040;
    --paper: #fbfbf9;
    --brand-blue: #2f5f8e;
    --brand-red: #b3262d;
    --rule: #c9ced6;
    --sky: #dce8f3;
    --ink: #2a2f38;
  }
  * { box-sizing: border-box; margin: 0; padding: 0; }
  html, body { width: 1200px; height: 900px; overflow: hidden; }
  body {
    background: var(--backdrop);
    font-family: "Montserrat", sans-serif;
    position: relative;
  }
  .card {
    position: absolute;
    left: 250px;
    width: 700px;
    height: 400px;
    background: var(--paper);
    overflow: hidden;
    box-shadow: 0 6px 18px rgba(0,0,0,.35);
  }
  .card--front { top: 35px; }
  .card--back { top: 465px; }

  .brand {
    position: absolute;
    display: flex;
    align-items: center;
    gap: 16px;
  }
  .brand__dot {
    width: 48px; height: 48px;
    border-radius: 50%;
    background: var(--brand-red);
    flex: none;
  }
  .brand__name {
    color: var(--brand-blue);
    font-weight: 500;
    line-height: 1.05;
  }
  .card--front .brand { left: 90px; top: 70px; }
  .card--front .brand__name { font-size: 40px; }
  .card--back .brand { left: 40px; top: 150px; }
  .card--back .brand__name { font-size: 28px; }
  .card--back .brand__dot { width: 40px; height: 40px; }

  .banner-photo {
    position: absolute;
    left: 0; right: 0;
    top: 215px; height: 135px;
    background: linear-gradient(90deg, var(--sky) 0%, #e6eef5 30%, #e3c3a6 55%, #d9a985 75%, #eedcc9 100%);
  }

  .divider {
    position: absolute;
    left: 330px; top: 30px;
    width: 1px; height: 290px;
    background: var(--rule);
  }
  .person {
    position: absolute;
    left: 365px; top: 75px;
  }
  .person__name {
    color: var(--brand-blue);
    font-weight: 600;
    font-size: 22px;
    letter-spacing: 3px;
    text-transform: uppercase;
  }
  .person__title {
    color: var(--ink);
    font-size: 14px;
    letter-spacing: 1px;
    margin-top: 4px;
  }
  .contacts {
    position: absolute;
    left: 365px; top: 210px;
    list-style: none;
  }
  .contacts li {
    display: flex;
    align-items: center;
    gap: 14px;
    font-size: 15px;
    letter-spacing: 1px;
    color: var(--ink);
    height: 28px;
  }
  .contacts svg { width: 13px; height: 13px; flex: none; }
  .tagline-band {
    position: absolute;
    left: 0; right: 0; bottom: 0;
    height: 40px;
    background: var(--brand-blue);
    color: #fff;
    font-size: 14px;
    letter-spacing: 1px;
    display: flex;
    align-items: center;
    justify-content: center;
    white-space: nowrap;
  }
</style>
</head>
<body>
  <section class="card card--front">
    <div class="brand">
      <span class="brand__dot"></span>
      <span class="brand__name">Healer at<br>the Hearth</span>
    </div>
    <div class="banner-photo" role="img" aria-label="Banner photo of clasped caring hands on a soft blue background"></div>
  </section>

  <section class="card card--back">
    <div class="brand">
      <span class="brand__dot"></span>
      <span class="brand__name">Healer at<br>the Hearth</span>
    </div>
    <div class="divider"></div>
    <div class="person">
      <p class="person__name">Daniel Marsh</p>
      <p class="person__title">Title,Department</p>
    </div>
    <ul class="contacts">
      <li>
        <svg viewBox="0 0 16 16"><path fill="#b3262d" d="M3 1l3 3-2 2c1 2 4 5 6 6l2-2 3 3-2 2C7 15 1 9 2 3z"/></svg>
        555-014-2290
      </li>
      <li>
        <svg viewBox="0 0 16 16"><rect x="1" y="3" width="14" height="10" fill="none" stroke="#b3262d" stroke-width="1.6"/><path d="M1 3l7 6 7-6" fill="none" stroke="#b3262d" stroke-width="1.6"/></svg>
        info@healerathearth.ca
      </li>
      <li>
        <svg viewBox="0 0 16 16"><circle cx="8" cy="8" r="6.5" fill="none" stroke="#b3262d" stroke-width="1.5"/><ellipse cx="8" cy="8" rx="3" ry="6.5" fill="none" stroke="#b3262d" stroke-width="1.2"/><path d="M1.5 8h13" stroke="#b3262d" stroke-width="1.2"/></svg>
        www.healerathearth.ca
      </li>
    </ul>
    <div class="tagline-band">We stand by your side, share the weight and guide you through every step of care.</div>
  </section>
</body>
</html>
```